Health Coach needs a Business Card Design

Need a really modern feminine business card design for a health and lifestyle coach. Needs to use geometric shapes, muted grey/blue/green pastels and black and white - see mood board attached and logo. The client likes black and white, modern, san serif with the use of lines and possibly a shadow leaf as in the mood board. Possibly put the tag line on the back or an icon of the logo. Logo is also attached. An icon of the logo would be great too.

Target Market(s)

Women (some men) aged 30 to 50.

Industry/Entity Type

Business

Contact Information for Business Card

Marla Teveny
e-mail: hello@marlatwell.example
website: marlatwell.example
Phone: +610497258316

The tag line is "A calmer body for living"

Font styles to use
Sans Serif

Colors
ecf7fb
cfeae6
000000
ffffff
f5f5f5

Requirements
Must have
• Black and white, logo, tag line and details
Nice to have
• Would be nice to incorporate the shadow palm.fern leaves as in the mood board and or geometric lines/shapes - see mood board. Could be either standard rectangle or would be happy with square too.
Should not have
• Flowers or decorations

```html
<!DOCTYPE html>
<html lang="en">
<head>
<meta charset="utf-8">
<title>Marla Teveny — Business Card</title>
<link rel="stylesheet" href="https://fonts.googleapis.com/css2?family=Cinzel:wght@400&family=Josefin+Sans:wght@300&display=swap">
<style>
  :root {
    --page: #d9dcde;
    --ink: #000000;
    --paper: #ffffff;
    --paper-soft: #f5f5f5;
    --mist: #ecf7fb;
    --sage: #cfeae6;
    --grey-dark: #1c1c1c;
  }
  * { box-sizing: border-box; margin: 0; padding: 0; }
  html, body { width: 1200px; height: 840px; overflow: hidden; }
  body {
    background: var(--page);
    display: flex;
    align-items: center;
    justify-content: center;
    gap: 80px;
  }
  .card {
    width: 340px;
    height: 612px;
    position: relative;
    overflow: hidden;
    box-shadow: 0 10px 30px rgba(0,0,0,0.18);
  }

  /* Front */
  .card-front {
    background: linear-gradient(160deg, var(--paper) 0%, var(--paper-soft) 40%, #e4e4e4 70%, var(--paper) 100%);
  }
  .geo-texture {
    position: absolute; inset: 0;
    background: linear-gradient(125deg, rgba(255,255,255,0.7) 0%, rgba(230,230,230,0.4) 45%, rgba(255,255,255,0.5) 100%);
  }
  .brand {
    position: absolute; top: 140px; left: 0; right: 0;
    text-align: center;
  }
  .brand-name {
    font-family: "Josefin Sans", sans-serif;
    font-weight: 300;
    font-size: 36px;
    letter-spacing: 2px;
    line-height: 40px;
    color: var(--ink);
  }
  .brand-rule {
    display: block; margin: 4px auto 8px;
    width: 200px; height: 1px; background: var(--ink);
  }
  .tagline-front {
    font-family: "Josefin Sans", sans-serif;
    font-weight: 300;
    font-size: 10px;
    letter-spacing: 3px;
    text-transform: uppercase;
    color: var(--grey-dark);
  }
  .scene-band {
    position: absolute; top: 226px; left: 0; right: 0; height: 170px;
    background: linear-gradient(90deg, #1a1a1a 0%, #6e6e6e 30%, #d8d8d8 50%, #6e6e6e 70%, #1a1a1a 100%);
  }
  .details {
    position: absolute; top: 424px; left: 0; right: 0;
    text-align: center;
    font-family: "Cinzel", serif;
    color: var(--ink);
  }
  .person-name {
    font-size: 13px; letter-spacing: 5px; text-transform: uppercase;
    margin-bottom: 18px;
  }
  .contact-line {
    font-size: 10px; letter-spacing: 3px; text-transform: uppercase;
    line-height: 15px;
  }

  /* Back */
  .card-back { background: var(--ink); }
  .glow-photo {
    position: absolute; inset: 0;
    background: radial-gradient(circle at 62% 64%, #ffffff 0%, #e6e6e6 4%, #7a7a7a 12%, #2a2a2a 28%, var(--ink) 50%);
  }
  .tagline-back {
    position: absolute;
    left: 48px; top: 306px;
    transform: translate(-50%, -50%) rotate(-90deg);
    white-space: nowrap;
    font-family: "Josefin Sans", sans-serif;
    font-weight: 300;
    font-size: 17px;
    letter-spacing: 3px;
    text-transform: uppercase;
    color: var(--paper);
  }
</style>
</head>
<body>
  <section class="card card-front">
    <div class="geo-texture" role="img" aria-label="Soft light grey low-poly geometric background"></div>
    <div class="brand">
      <div class="brand-name">Marla T</div>
      <span class="brand-rule"></span>
      <div class="tagline-front">A calmer body for living</div>
    </div>
    <div class="scene-band" role="img" aria-label="Black and white illustration of a figure with an umbrella in falling rain between trees"></div>
    <div class="details">
      <div class="person-name">Marla Teveny</div>
      <div class="contact-line">hello@marlatwell.example</div>
      <div class="contact-line">marlatwell.example</div>
      <div class="contact-line">+610497258316</div>
    </div>
  </section>

  <section class="card card-back">
    <div class="glow-photo" role="img" aria-label="Dark photograph of a single glowing light bulb among unlit bulbs"></div>
    <div class="tagline-back">A calmer body for living</div>
  </section>
</body>
</html>
```